Business Card Design for new social media business

I am looking for a new professional business card design for an exciting new company which is based on providing members with experiences of others to benefit their choice of places to visit for restaurants, bars, clubs, national monument, tourist sights, hotels and so forth.
Updates

Please submit designs as I will choose to commit the funds depending on designs.

Reason: More designs required

Target Market(s)

Business Managers as well as directors alongside owners

Industry/Entity Type

Business

Requirements
Must have
• Logo design and symbols
Nice to have
• Logo / Symbol on the back of the business card and possibly the logo as if embedded/embossed on the business card.

```html
<!DOCTYPE html>
<html lang="en">
<head>
<meta charset="utf-8">
<title>Viewnest Business Card</title>
<link rel="stylesheet" href="https://fonts.googleapis.com/css2?family=Barlow:wght@400;500;700&display=swap">
<style>
  :root {
    --page-bg: #e9e9eb;
    --card-white: #ffffff;
    --card-dark: #262626;
    --brand-blue: #2f5fd0;
    --map-blue-deep: #122a5c;
    --map-blue-mid: #1d3f85;
    --text-grey: #4a4a4a;
    --text-dark: #2b2b2b;
    --divider: #3b6fd8;
  }
  * { box-sizing: border-box; margin: 0; padding: 0; }
  html, body {
    width: 1200px;
    height: 1000px;
    overflow: hidden;
    background: var(--page-bg);
    font-family: "Barlow", Arial, sans-serif;
  }
  .canvas {
    position: relative;
    width: 1200px;
    height: 1000px;
  }
  .card {
    position: absolute;
    top: 350px;
    width: 525px;
    height: 300px;
    border-radius: 4px;
    box-shadow: 0 6px 18px rgba(0,0,0,0.12);
    overflow: hidden;
  }
  .card-front { left: 50px; background: var(--card-white); }
  .card-back { left: 625px; background: var(--card-dark); }

  .brand {
    position: absolute;
    display: flex;
    align-items: center;
    gap: 10px;
  }
  .brand-dot {
    width: 34px;
    height: 34px;
    border-radius: 50%;
    background: var(--brand-blue);
  }
  .brand-name {
    font-weight: 700;
    font-size: 40px;
    color: var(--brand-blue);
    letter-spacing: -0.5px;
    line-height: 1;
  }
  .card-front .brand { left: 40px; top: 62px; }

  .holder-name {
    position: absolute;
    left: 170px;
    top: 176px;
    font-size: 22px;
    font-weight: 400;
    color: var(--text-dark);
    letter-spacing: 0.3px;
  }
  .divider {
    position: absolute;
    left: 322px;
    top: 95px;
    width: 1.5px;
    height: 110px;
    background: var(--divider);
  }
  .contact-list {
    position: absolute;
    left: 340px;
    top: 100px;
    list-style: none;
  }
  .contact-item {
    display: flex;
    align-items: center;
    gap: 10px;
    height: 24px;
    font-size: 14px;
    color: var(--text-grey);
  }
  .contact-icon { width: 13px; height: 13px; flex: none; }

  .world-map {
    position: absolute;
    left: 20px;
    top: 20px;
    width: 485px;
    height: 260px;
    border-radius: 6px;
    background: radial-gradient(ellipse at 55% 40%, var(--map-blue-mid) 0%, var(--map-blue-deep) 55%, rgba(18,42,92,0) 85%);
    opacity: 0.75;
  }
  .card-back .brand { left: 188px; top: 170px; }
  .card-back .brand-dot { width: 30px; height: 30px; }
  .card-back .brand-name { font-size: 34px; }
</style>
</head>
<body>
<main class="canvas">
  <section class="card card-front" aria-label="Business card front">
    <div class="brand">
      <span class="brand-dot"></span>
      <span class="brand-name">Viewnest</span>
    </div>
    <p class="holder-name">Arjun Mehra</p>
    <span class="divider"></span>
    <ul class="contact-list">
      <li class="contact-item">
        <svg class="contact-icon" viewBox="0 0 16 16" aria-hidden="true"><path fill="#2f5fd0" d="M3.5 1h3l1 4-2 1.3a8 8 0 0 0 4.2 4.2L11 8.5l4 1v3c0 1-1 2-2 2A13 13 0 0 1 1.5 3c0-1 1-2 2-2z"/></svg>
        <span>555.010.2486</span>
      </li>
      <li class="contact-item">
        <svg class="contact-icon" viewBox="0 0 16 16" aria-hidden="true"><rect x="1" y="3" width="14" height="10" rx="1" fill="#2f5fd0"/><path d="M1.5 3.5 8 9l6.5-5.5" fill="none" stroke="#fff" stroke-width="1.3"/></svg>
        <span>amehra@viewnest.com</span>
      </li>
      <li class="contact-item">
        <svg class="contact-icon" viewBox="0 0 16 16" aria-hidden="true"><circle cx="8" cy="8" r="7" fill="#2f5fd0"/><path d="M1 8h14M8 1c-2.5 2-2.5 12 0 14M8 1c2.5 2 2.5 12 0 14" fill="none" stroke="#fff" stroke-width="1"/></svg>
        <span>www.viewnest.com</span>
      </li>
    </ul>
  </section>

  <section class="card card-back" aria-label="Business card back">
    <div class="world-map" role="img" aria-label="Pixel-style world map in dark blue squares"></div>
    <div class="brand">
      <span class="brand-dot"></span>
      <span class="brand-name">Viewnest</span>
    </div>
  </section>
</main>
</body>
</html>
```